Geschäftspapiere für Rechtsanwaltskanzlei
Zielgruppe
Rechtsanwaltskanzlei als Einzelkanzlei, Schwerpunkt: Immobilienrecht
Aufgabenstellung
Das Design soll modern abstrakt sein und Stärke und Kompromisslosigkeit assoziieren ( wie das bereits vorhandene Logo). Die Informationen im vorhandenen Briefbogen müssen alle übernommen werden.
Wir benötigen 4 Betreffzeilen: Unser Zeichen, Ihr Zeichen, wer ./.wen und kurze Beschreibung des Falles.
Das schwarze Logo soll übernommen werden, gerne hätten wir noch eine zweite Farbe ( rot oder blau ) im Briefbogen in Form von Balken oder Hervorhebung von Text.

```html
<!DOCTYPE html>
<html lang="de">
<head>
<meta charset="utf-8">
<title>Briefbogen Velmhaus Rechtsanwaltskanzlei</title>
<link rel="stylesheet" href="https://fonts.googleapis.com/css2?family=Open+Sans:wght@400;600;700&family=Playfair+Display&display=swap">
<style>
  :root {
    --backdrop: #dcdadd;
    --paper: #ffffff;
    --ink: #0a0a0c;
    --accent: #3a7bc8;
    --faint: #f5f5f5;
  }
  * { margin: 0; padding: 0; box-sizing: border-box; }
  html, body { width: 1200px; height: 1200px; overflow: hidden; background: var(--backdrop); }
  body { position: relative; font-family: "Open Sans", sans-serif; color: var(--ink); }
  .sheet { position: absolute; left: 302px; top: 179px; width: 595px; height: 841px; background: var(--paper); }
  .abs { position: absolute; }
  .brand { left: 68px; top: 28px; display: flex; align-items: center; gap: 8px; }
  .brand-square { width: 40px; height: 40px; background: var(--ink); }
  .brand-name { font-weight: 700; font-size: 30px; letter-spacing: 2px; color: var(--ink); line-height: 1; }
  .brand-sub { left: 68px; top: 89px; font-size: 12.5px; font-weight: 600; letter-spacing: 0.3px; }
  .rule { left: 68px; width: 499px; height: 1px; background: var(--accent); }
  .sender { left: 68px; top: 141px; font-size: 5.6px; line-height: 8px; }
  .sender b { color: var(--accent); font-weight: 700; }
  .refs { left: 354px; top: 140px; font-size: 7.8px; line-height: 12px; font-weight: 600; color: var(--accent); }
  .refs .gap { height: 12px; }
  .fold { left: 0; width: 20px; height: 1px; }
  .fold-blue { top: 297px; background: var(--accent); }
  .fold-ink { top: 420px; background: var(--ink); }
  .backdrop-name { left: 186px; top: 358px; width: 224px; height: 126px; display: flex; align-items: center; justify-content: center; font-weight: 700; font-size: 64px; letter-spacing: 4px; color: var(--faint); }
  .footer-col { top: 714px; font-size: 6.9px; line-height: 9px; }
  .footer-col .head { color: var(--accent); font-weight: 600; }
  .footer-col b { font-weight: 700; }
  .footer-col .row { display: flex; }
  .footer-col .row span:first-child { width: 29px; flex: none; }
  .col-firm { left: 68px; }
  .col-east { left: 189px; }
  .col-north { left: 323px; }
  .col-bank { left: 456px; }
  .col-bank .row span:first-child { width: 21px; }
  .focus-band { left: 68px; top: 798px; width: 499px; height: 43px; background: var(--ink); color: #fff; display: flex; align-items: center; justify-content: center; font-size: 13.6px; font-weight: 600; letter-spacing: 0.2px; word-spacing: 1px; }
</style>
</head>
<body>
  <div class="sheet">
    <div class="abs brand"><div class="brand-square"></div><div class="brand-name">VELMHAUS</div></div>
    <div class="abs brand-sub">RECHTSANWALTSKANZLEI</div>
    <div class="abs rule" style="top:116px"></div>

    <div class="abs sender"><b>Velmhaus Rechtsanwaltskanzlei</b> | Helena Marwitz-Oberg<br>Lindauer Hangweg 212b | 51069 Köln (Dellbrück)</div>

    <div class="abs refs">
      <div>Ihr Zeichen:</div>
      <div>Ihre Nachricht vom:</div>
      <div>Unser Zeichen:</div>
      <div>Unsere Nachricht vom:</div>
      <div>Beschreibung des Falles:</div>
      <div class="gap"></div>
      <div>Name:</div>
      <div>Telefon:</div>
      <div>Telefax:</div>
      <div>E-Mail:</div>
      <div class="gap"></div>
      <div>Datum:</div>
    </div>

    <div class="abs fold fold-blue"></div>
    <div class="abs fold fold-ink"></div>

    <div class="abs backdrop-name" aria-hidden="true">VELMHAUS</div>

    <div class="abs rule" style="top:700px"></div>

    <div class="abs footer-col col-firm">
      <div class="head">Velmhaus Anwaltskanzlei</div>
      <div>&nbsp;</div>
      <div><b>Rechtsanwältin</b></div>
      <div><b>Helena Marwitz-Oberg</b></div>
      <div>Fachanwältin für Mietrecht</div>
      <div>und WEG-Recht</div>
    </div>
    <div class="abs footer-col col-east">
      <div class="head">Büro Köln-Mülheim</div>
      <div>Falkener Straße 37</div>
      <div>51063 Köln</div>
      <div class="row"><span>Telefon:</span><span>+49 (0) 221 318 502 64</span></div>
      <div class="row"><span>Telefax:</span><span>+49 (0) 221 590 73 18</span></div>
      <div class="row"><span>Mobil:</span><span>+49 (0) 1577 862 04 39</span></div>
      <div class="row"><span>E-Mail:</span><span>info@velmhaus-kanzlei.de</span></div>
    </div>
    <div class="abs footer-col col-north">
      <div class="head">Büro Köln Dellbrück</div>
      <div>Lindauer Hangweg 212b</div>
      <div>51069 Köln</div>
      <div class="row"><span>Telefon:</span><span>+49 (0) 221 4861027</span></div>
      <div class="row"><span>Telefax:</span><span>+49 (0) 221 590 73 18</span></div>
      <div class="row"><span>Mobil:</span><span>+49 (0) 1577 862 04 39</span></div>
      <div class="row"><span>E-Mail:</span><span>info@velmhaus-kanzlei.de</span></div>
    </div>
    <div class="abs footer-col col-bank">
      <div class="head">Bankverbindung:</div>
      <div>Stadtbank Rheinufer</div>
      <div class="row"><span>IBAN:</span><span>DE41370400220618473905</span></div>
      <div class="row"><span>BIC:</span><span>RHUFDE21XXX</span></div>
    </div>

    <div class="abs rule" style="top:790px"></div>
    <div class="abs focus-band">Mietrecht | Wohnungseigentumsrecht | Baurecht | Grundstücksrecht</div>
  </div>
</body>
</html>
```